Velvet & Bloom Hair Extensions needs a business card

We need a business card designed for an online luxury hair extensions business called Velvet & Bloom, we already have a logo and need an innovative business card (2-sided preferably). The strap line for the brand is 'Effortless Hair For Every Moment!'. The brand is a premium brand selling virgin hair extensions and the target market is the mid-affluent ethnic woman as such the design should reflect this. The brand logo is grey and can be sent when requested.

Target Market(s)

25 to 35 year mid-affluent ethnic woman (Afro-American, Mixed Race, Asian)

Industry/Entity Type

Hair

Colors

Designer to choose colors to be used in the design.

Requirements
Must have
• Business Name: Velvet and Bloom
Strapline: Effortless Hair For Every Moment!
Domain: ​www.velvetandbloom-demo.com
Email: info@velvetandbloom-demo.com
sales and enquiries
44 07391 xxxxxxx

Please use the grey main brand logo depicted in page 2 of the attached pdf document

```html
<!DOCTYPE html>
<html lang="en">
<head>
<meta charset="utf-8">
<title>Velvet &amp; Bloom – Business Card</title>
<link rel="stylesheet" href="https://fonts.googleapis.com/css2?family=Raleway:ital,wght@0,400;0,500;1,300&display=swap">
<style>
  :root {
    --backdrop: #2a2b2d;
    --card: #f4f4f3;
    --card-edge: #e2e2e1;
    --band-start: #a4a8ac;
    --band-end: #c2c5c8;
    --art-deep: #9a9ea2;
    --art-soft: rgba(170,174,178,0);
    --brand-grey: #85898d;
    --strap-grey: #6d7175;
    --ink: #2f3133;
    --white: #ffffff;
  }
  * { margin: 0; padding: 0; box-sizing: border-box; }
  html, body { width: 1200px; height: 678px; overflow: hidden; }
  body {
    background: var(--backdrop);
    font-family: "Raleway", "Helvetica Neue", Arial, sans-serif;
    position: relative;
  }
  .card {
    position: absolute;
    top: 184px;
    width: 540px;
    height: 310px;
    background: linear-gradient(135deg, var(--white), var(--card) 60%, var(--card-edge));
    border-radius: 3px;
    overflow: hidden;
    box-shadow: 0 14px 30px rgba(0,0,0,.45);
  }
  .card--contact { left: 40px; }
  .card--brand { left: 620px; }

  .band {
    position: absolute;
    background: linear-gradient(90deg, var(--band-start), var(--band-end));
  }
  .card--contact .band { left: 0; top: 82px; width: 100%; height: 150px; }
  .card--brand .band { left: 0; top: 78px; width: 390px; height: 160px; }

  .hair-art {
    position: absolute;
    border-radius: 40% 40% 30% 30%;
    background: radial-gradient(ellipse at 50% 40%, var(--art-deep), var(--art-soft) 72%);
  }
  .card--contact .hair-art { left: 90px; top: 30px; width: 190px; height: 240px; }
  .card--brand .hair-art { left: 320px; top: 18px; width: 190px; height: 225px; }

  .strapline {
    position: absolute;
    font-style: italic;
    font-weight: 300;
    letter-spacing: .3px;
  }
  .card--contact .strapline { top: 20px; right: 24px; font-size: 15px; color: var(--strap-grey); }
  .card--brand .strapline { top: 200px; left: 24px; font-size: 17px; color: var(--white); }

  .email {
    position: absolute;
    top: 100px; left: 190px;
    display: flex; align-items: center; gap: 8px;
    font-size: 19px; color: var(--white);
  }
  .email svg { width: 24px; height: 17px; }

  .sales {
    position: absolute;
    top: 150px; left: 252px;
    color: var(--white);
  }
  .sales__label { font-size: 14px; letter-spacing: 1.4px; text-transform: uppercase; }
  .sales__phone { font-size: 29px; letter-spacing: .5px; line-height: 1.1; }

  .brand-name {
    position: absolute;
    display: flex; align-items: center; gap: 10px;
    font-weight: 500;
    text-transform: uppercase;
    letter-spacing: 2px;
    color: var(--brand-grey);
  }
  .brand-name__dot { width: 12px; height: 12px; border-radius: 50%; background: var(--brand-grey); }
  .card--contact .brand-name { top: 242px; left: 26px; font-size: 24px; }
  .card--brand .brand-name { top: 252px; right: 24px; font-size: 24px; }

  .website {
    position: absolute;
    top: 276px; left: 26px;
    font-size: 17px; color: var(--ink); letter-spacing: .3px;
  }
</style>
</head>
<body>
  <section class="card card--contact" aria-label="Business card, contact side">
    <div class="band"></div>
    <div class="hair-art" role="img" aria-label="Grey illustration of a woman's flowing hair"></div>
    <p class="strapline">Effortless Hair For Every Moment!</p>
    <p class="email">
      <svg viewBox="0 0 24 17" aria-hidden="true"><rect x="0.5" y="0.5" width="23" height="16" fill="var(--white)"/><path d="M1 1 L12 10 L23 1" fill="none" stroke="var(--band-start)" stroke-width="1.4"/></svg>
      info@velvetandbloom-demo.com
    </p>
    <div class="sales">
      <p class="sales__label">Sales and Enquiries</p>
      <p class="sales__phone">07391 480217</p>
    </div>
    <p class="brand-name"><span class="brand-name__dot"></span>Velvet &amp; Bloom</p>
    <p class="website">www.velvetandbloom-demo.com</p>
  </section>

  <section class="card card--brand" aria-label="Business card, brand side">
    <div class="band"></div>
    <div class="hair-art" role="img" aria-label="Grey illustration of a woman's flowing hair"></div>
    <p class="strapline">Effortless Hair For Every Moment!</p>
    <p class="brand-name"><span class="brand-name__dot"></span>Velvet &amp; Bloom</p>
  </section>
</body>
</html>
```